Ronan Pike Building Business Card Design

Hi,

I need a business card for my Building company.
I am a Builder and build homes for clients.
I am looking for a sophisticated logo that can be used on business cards, envelopes and letter heads.
I am trying to take my business to the next level and need a professional business card.

Colours: Please use white, black, dark grey and bright blue.

Thank you,

Marnie and Ronan.

Target Market(s)

1. Home and Building Companies 2. Potential customers

Industry/Entity Type

Business

Contact Information for Business Card

Ronan Pike Building PTY LTD

Ronan Pike

Director

A.B.N. 37 902 518 617

BUILDERS LICENCE No. 573019k

Mobile: 0471 283 906

Email: ronanpikebuilding@maildrop-example.com.au

Requirements
Must have
• The following is compulsory to have in the designs:

Ronan Pike Building PTY LTD (business name)

Ronan Pike (contact name)

Director (position)

A.B.N. 37 902 518 617

Builders Licence No. 573019k

Mobile: 0471 283 906

Nice to have
• Logo for business
Should not have
• Should not be cluttered.

I am looking for a clean, sophisticated and professional business card design.

```html
<!DOCTYPE html>
<html lang="en">
<head>
<meta charset="utf-8">
<title>Ronan Pike Building – Business Cards</title>
<link rel="stylesheet" href="https://fonts.googleapis.com/css2?family=Cabin:wght@400;600;700&display=swap">
<style>
  :root {
    --stage: #3a3a3a;
    --brand-blue: #1f72c0;
    --brand-blue-text: #1f5fa8;
    --charcoal: #3c3c3c;
    --ink: #1e1e1e;
    --paper: #ffffff;
    --muted: #4a4a4a;
  }
  * { margin: 0; padding: 0; box-sizing: border-box; }
  html, body {
    width: 1200px; height: 949px; overflow: hidden;
    background: var(--stage);
    font-family: "Cabin", "Gill Sans", sans-serif;
  }
  .stage {
    position: relative; width: 1200px; height: 949px;
    display: flex; align-items: center; justify-content: center; gap: 50px;
  }
  .card {
    position: relative; width: 540px; height: 330px;
    box-shadow: 0 8px 24px rgba(0,0,0,.45);
    overflow: hidden;
  }
  /* Front card */
  .card--front { background: var(--brand-blue); }
  .card--front .side-band {
    position: absolute; left: 0; top: 0; bottom: 0; width: 34px;
    background: var(--charcoal);
  }
  .brand {
    display: flex; align-items: center; gap: 10px;
    font-weight: 700; color: var(--ink); letter-spacing: .5px;
  }
  .brand__square { width: 18px; height: 18px; background: var(--paper); flex: none; }
  .card--front .brand {
    position: absolute; right: 46px; top: 40px; font-size: 34px;
  }
  .company-block {
    position: absolute; right: 46px; top: 100px;
    text-align: right; color: var(--ink); font-size: 15px; line-height: 1.35;
  }
  .company-block .company-name { color: var(--paper); letter-spacing: .3px; }
  .contact {
    position: absolute; left: 66px; bottom: 34px; color: var(--paper);
    font-size: 14px; line-height: 1.45;
  }
  .contact__name { font-size: 22px; font-weight: 700; line-height: 1.2; }
  .contact__role { color: var(--ink); font-size: 13px; margin-bottom: 2px; }
  .contact__row span { display: inline-block; width: 52px; }

  /* Back card */
  .card--back { background: var(--paper); }
  .card--back .corner-tab {
    position: absolute; right: 0; top: 0; width: 30px; height: 56px;
    background: var(--brand-blue);
  }
  .logo-lockup {
    position: absolute; left: 38px; top: 118px; width: 220px;
  }
  .card--back .brand { font-size: 32px; }
  .card--back .brand__square { background: var(--brand-blue); }
  .logo-lockup__sub {
    margin-top: 14px; font-size: 12px; color: var(--muted); letter-spacing: .6px;
  }
  .divider {
    position: absolute; left: 272px; top: 106px; width: 2px; height: 132px;
    background: var(--ink);
  }
  .details {
    position: absolute; left: 292px; top: 134px;
    font-size: 14.5px; line-height: 1.45; color: var(--ink);
  }
  .details .highlight { color: var(--brand-blue-text); }
</style>
</head>
<body>
<main class="stage">
  <section class="card card--front" aria-label="Business card front">
    <div class="side-band"></div>
    <div class="brand"><span class="brand__square"></span>Ronan Pike</div>
    <div class="company-block">
      <p class="company-name">RONAN PIKE BUILDING PTY LTD</p>
      <p>A.B.N. 37 902 518 617</p>
      <p>Builders Licence No. 573019k</p>
    </div>
    <div class="contact">
      <p class="contact__name">Ronan Pike</p>
      <p class="contact__role">Managing Director</p>
      <p class="contact__row"><span>Mobile:</span>0471 283 906</p>
      <p class="contact__row"><span>Email:</span>ronanpikebuilding@maildrop-example.com.au</p>
    </div>
  </section>

  <section class="card card--back" aria-label="Business card back">
    <div class="corner-tab"></div>
    <div class="logo-lockup">
      <div class="brand"><span class="brand__square"></span>Ronan Pike</div>
      <p class="logo-lockup__sub">RONAN PIKE BUILDING PTY LTD</p>
    </div>
    <div class="divider"></div>
    <div class="details">
      <p><span class="highlight">Ronan Pike Building</span> PTY LTD</p>
      <p>A.B.N. 37 902 518 617</p>
      <p>Builders Licence No. 573019k</p>
    </div>
  </section>
</main>
</body>
</html>
```